Cedar Hall letterhead

We changed our name and logo now need letterhead.
3-4/72 Harlow Street Marrowdale 2163
www.cedarhall.org.au
info@cedarhall.org.au
ph: 02 97584120

At this stage, we are preferencing Design #: 5398880 and Design #5401338

```html
<!DOCTYPE html>
<html lang="en">
<head>
<meta charset="utf-8">
<title>Cedar Hall Letterhead</title>
<link rel="stylesheet" href="https://fonts.googleapis.com/css2?family=Quicksand:wght@400;700&family=Ubuntu:wght@500&display=swap">
<style>
  :root {
    --backdrop: #e9e6e1;
    --label: #4a3d33;
    --paper: #ffffff;
    --slate-sheet: #a8bac6;
    --slate-mark: #7d93a6;
    --slate-band: #7b8896;
    --ink: #1c232a;
  }
  * { margin: 0; padding: 0; box-sizing: border-box; }
  html, body { width: 1200px; height: 900px; overflow: hidden; }
  body {
    position: relative;
    background: var(--backdrop);
    font-family: "Quicksand", sans-serif;
  }
  .side-label {
    position: absolute;
    top: 60px;
    font-family: "Ubuntu", sans-serif;
    font-weight: 500;
    font-size: 27px;
    color: var(--label);
    transform: translateX(-50%);
  }
  .side-label--front { left: 317px; }
  .side-label--back { left: 845px; }

  .sheet {
    position: absolute;
    top: 111px;
    width: 491px;
    height: 695px;
    box-shadow: 0 2px 6px rgba(0,0,0,0.18);
  }
  .sheet--front { left: 95px; background: var(--paper); }
  .sheet--back { left: 611px; background: var(--slate-sheet); }

  .brand {
    position: absolute;
    left: 20px;
    bottom: 24px;
    display: flex;
    align-items: center;
    gap: 10px;
  }
  .brand__dot {
    width: 38px;
    height: 38px;
    border-radius: 50%;
    background: var(--slate-mark);
  }
  .brand__name {
    font-size: 19px;
    font-weight: 400;
    color: var(--slate-mark);
    letter-spacing: 1px;
    text-transform: uppercase;
  }

  .contact-arrow {
    position: absolute;
    left: 550px;
    top: 744px;
    width: 226px;
    height: 26px;
  }
  .contact-arrow__label {
    position: absolute;
    right: 8px;
    top: 50%;
    transform: translateY(-50%);
    font-size: 7px;
    font-weight: 700;
    color: var(--ink);
  }
  .contact-details {
    position: absolute;
    left: 788px;
    top: 739px;
    font-size: 8.5px;
    line-height: 10px;
    color: var(--ink);
    list-style: none;
  }
</style>
</head>
<body>
  <div class="side-label side-label--front">Front</div>
  <div class="side-label side-label--back">Back</div>

  <section class="sheet sheet--front">
    <div class="brand">
      <span class="brand__dot"></span>
      <span class="brand__name">Cedar Hall</span>
    </div>
  </section>

  <section class="sheet sheet--back"></section>

  <div class="contact-arrow">
    <svg width="226" height="26" viewBox="0 0 226 26" aria-hidden="true">
      <polygon points="0,13 22,0 22,3 226,3 226,23 22,23 22,26" fill="var(--slate-band)"/>
    </svg>
    <span class="contact-arrow__label">Contact Us:</span>
  </div>

  <ul class="contact-details">
    <li>3-4/72 Harlow Street Marrowdale 2163</li>
    <li>www.cedarhall.org.au</li>
    <li>info@cedarhall.org.au</li>
    <li>Ph: 02 97584120</li>
  </ul>
</body>
</html>
```